依頼概要
■依頼の目的/概要
当方、飲食店を4店舗経営しております
1.創作居酒屋
2.イタリアン+鮨
3.和食居酒屋
4.鮨+鉄板焼
以上4店舗です。
この度、新型コロナウイルスの影響で
お客様がご来店されなくなり
急遽、テイクアウトとデリバリーに力を
入れていこうと決めました。
そこで、魅力のあるメニューを作りたい
と考えております。
■要望のポイント
今回のメニューは先程あげました4店舗のメニューがそれぞれ入っております。
和と洋をイメージできるような、おしゃれな感じを望んでいます。お客様の層は幅広いですが、女性の方が多いです。
■その他注意点など
店内のイメージは
写真を送ることも可能ですが
菜ダイニング灯で検索していただけると
画像が出ると思います。
できればイメージの統一感があればいいなと思います。
メニューの内容や
写真はお送りいたします。
後ほど、写真の追加があります?
その他何かご不明点ただがあれば
お気軽にご質問ください
よろしくお願い致します
ロゴや料理写真を添付いたしました。
料理の写真は、店内メニュー用の写真なので
器とかが変わってしまいます。
ですので、このような料理です的なイメージみたいな感じでお願いできますでしょうか?
料理写真です。
宜しくお願いいたします。
ロゴです!
宜しくお願いいたします。
メニュー写真の追加です
全部の写真を使わなくても大丈夫です!
宜しくお願いいたします。
お弁当の写真です!
宜しくお願いいたします。
■ 選んだ理由

こちらの意向が伝わりやすく、イメージより良かったからです!!!

■ 提案者全員のお礼・コメント

毎月少しづつ内容やデザインを変えてやりたいと思っているので、またご縁があればうれしいなと思います!本当に素早いご対応ありがとうございます!

```html
<!DOCTYPE html>
<html lang="ja">
<head>
<meta charset="utf-8">
<title>テイクアウト＆デリバリー 菜ダイニング灯</title>
<link href="https://fonts.googleapis.com/css2?family=Shippori+Mincho:wght@500;700;800&family=Noto+Sans+JP:wght@400;500;700&family=Great+Vibes&display=swap" rel="stylesheet">
<style>
:root{
  --navy:#1c2340;
  --navy-deep:#141a33;
  --gold:#c9a35c;
  --pink:#e2879a;
  --red:#c8283a;
  --paper:#efece6;
  --card:#ffffff;
  --ink:#2b2b2b;
  --muted:#777;
  --photo-a:#5a3b25;
  --photo-b:#c98d4a;
}
*{margin:0;padding:0;box-sizing:border-box}
html,body{width:854px;height:1200px;overflow:hidden}
body{font-family:"Noto Sans JP",sans-serif;color:var(--ink);background:var(--paper)}
.flyer{position:relative;width:854px;height:1200px;overflow:hidden}
.header{position:absolute;left:0;top:0;width:854px;height:238px;background:linear-gradient(180deg,var(--navy-deep),var(--navy))}
.title{position:absolute;font-family:"Shippori Mincho",serif;font-weight:800;color:#fff;letter-spacing:2px;white-space:nowrap}
.title--takeout{left:48px;top:26px;font-size:64px}
.title--delivery{left:48px;top:112px;font-size:64px}
.title--started{right:44px;top:112px;font-size:62px}
.amp{position:absolute;left:300px;top:52px;font-family:"Great Vibes",cursive;font-size:110px;color:var(--pink);line-height:1}
.lead{position:absolute;left:0;width:854px;top:200px;text-align:center;font-family:"Shippori Mincho",serif;font-size:19px;color:var(--gold);font-weight:700}
.feature{position:absolute;left:42px;top:252px;width:770px;height:280px;background:var(--card);border:1px solid #d8d2c5}
.photo{position:absolute;background:linear-gradient(135deg,var(--photo-a),var(--photo-b) 60%,#7a5230)}
.photo--bento{left:12px;top:12px;width:400px;height:256px}
.badge{position:absolute;left:22px;top:40px;width:150px;height:150px;border-radius:50%;background:#fff;text-align:center;padding-top:24px;font-family:"Shippori Mincho",serif}
.badge small{display:block;font-size:12px;color:var(--muted)}
.badge .tag{display:inline-block;margin:6px 0;padding:2px 10px;background:var(--pink);color:#fff;font-size:13px}
.badge .price{font-size:26px;color:var(--red);font-weight:800}
.badge .price span{font-size:14px}
.badge .count{font-size:16px;font-weight:700}
.course-title{font-family:"Shippori Mincho",serif;font-weight:700;font-size:24px;color:var(--navy);text-align:center;border:1.5px solid var(--gold);border-radius:30px;padding:4px 0;background:#fff;white-space:nowrap}
.feature .course-title{position:absolute;left:470px;top:18px;width:250px}
.items{list-style:none;font-size:14px;line-height:1.72}
.items li{white-space:nowrap}
.items li::before{content:"・"}
.feature .items{position:absolute;left:460px;top:70px;font-size:13.5px;line-height:1.5}
.columns{position:absolute;left:42px;top:550px;width:770px;height:350px;display:flex;gap:14px}
.column{flex:1;background:var(--card);border:1px solid #d8d2c5;padding:18px 18px 0}
.column .items{margin-top:16px;font-size:14px}
.alacarte{position:absolute;left:200px;top:920px;width:454px;height:66px;border:1.5px solid var(--gold);background:#fff;text-align:center;font-family:"Shippori Mincho",serif;padding-top:9px}
.alacarte strong{display:block;font-size:19px}
.alacarte span{font-size:13px;color:var(--muted)}
.footer{position:absolute;left:0;top:1012px;width:854px;height:188px;background:#fff;border-top:4px solid var(--navy)}
.order{position:absolute;left:30px;top:24px;width:150px;background:var(--pink);color:#fff;font-size:14px;text-align:center;padding:6px 0;border-radius:3px;line-height:1.4}
.hours{position:absolute;left:214px;top:22px;font-family:"Shippori Mincho",serif;font-size:36px;font-weight:700;color:var(--navy);white-space:nowrap}
.shop{position:absolute;left:30px;top:100px;font-family:"Shippori Mincho",serif;font-size:36px;font-weight:800;color:var(--navy);white-space:nowrap}
.phone{position:absolute;right:30px;top:68px;display:flex;align-items:center;gap:8px;font-family:"Shippori Mincho",serif;font-size:46px;font-weight:800;color:var(--red);white-space:nowrap;line-height:1.1}
.address{position:absolute;right:30px;top:130px;font-size:12px;color:var(--muted);white-space:nowrap}
.pay{position:absolute;right:30px;top:154px;font-size:13px;display:flex;align-items:center;gap:6px;white-space:nowrap}
.pay i{width:12px;height:12px;background:var(--red);display:inline-block}
</style>
</head>
<body>
<div class="flyer">
  <header class="header">
    <div class="title title--takeout">テイクアウト</div>
    <div class="amp">&amp;</div>
    <div class="title title--delivery">デリバリー</div>
    <div class="title title--started">始めました！</div>
    <p class="lead">ご自宅でAKARIの特別なお食事をお楽しみください！</p>
  </header>

  <section class="feature">
    <div class="photo photo--bento" role="img" aria-label="灯御膳の弁当写真：刺身・天ぷら・焼物の詰め合わせ">
      <div class="badge">
        <small>おすすめ</small>
        <div class="price">3,000<span>円</span></div>
        <div class="tag">メニュー</div>
        <div class="count">4種</div>
      </div>
    </div>
    <h2 class="course-title">1. 灯御膳</h2>
    <ul class="items">
      <li>四川風麻婆豆腐</li>
      <li>天ぷら盛合わせ</li>
      <li>クリームコロッケ</li>
      <li>海老とホタテのタルタルサラダ</li>
      <li>お刺身３点盛</li>
      <li>玉子つくね</li>
      <li>鶏もも西京焼き</li>
      <li>黒毛和牛のステーキ</li>
      <li>トロサーモンのユッケ風サラダ</li>
    </ul>
  </section>

  <section class="columns">
    <div class="column">
      <h2 class="course-title">2. バルめし</h2>
      <ul class="items">
        <li>ナシゴレン</li>
        <li>天ぷら盛合わせ</li>
        <li>クリームコロッケ</li>
        <li>ロールキャベツ</li>
        <li>お刺身３点盛</li>
        <li>自家製ピクルス</li>
        <li>海老のタルタル焼き</li>
        <li>黒毛和牛ステーキ</li>
        <li>季節のサラダ</li>
      </ul>
    </div>
    <div class="column">
      <h2 class="course-title">3. 灯左衛門弁当</h2>
      <ul class="items">
        <li>黒毛和牛の肉じゃが</li>
        <li>天ぷら盛合わせ</li>
        <li>お刺身３点盛</li>
        <li>黒毛和牛と丸餅すき焼</li>
        <li>茶碗蒸し</li>
        <li>玉子つくね</li>
        <li>鶏もも西京焼き</li>
        <li>黒毛和牛ステーキ</li>
        <li>梅水晶お浸し</li>
      </ul>
    </div>
    <div class="column">
      <h2 class="course-title">4. 柊コース</h2>
      <ul class="items">
        <li>ホタテと野菜のマリネ</li>
        <li>茶碗蒸し</li>
        <li>生ハムとチーズ</li>
        <li>グリーンサラダ</li>
        <li>お刺身３点盛</li>
        <li>鶏もも西京焼き</li>
        <li>海老のタルタル焼き</li>
        <li>黒毛和牛ステーキ</li>
        <li>季節の甘味</li>
      </ul>
    </div>
  </section>

  <div class="alacarte">
    <strong>アラカルトのご用意もあります。</strong>
    <span>詳しくは裏面をご覧ください。</span>
  </div>

  <footer class="footer">
    <div class="order">ご注文・ご配送は<br>こちらまで</div>
    <div class="hours">17:00～22:00</div>
    <div class="shop">菜ダイニング灯</div>
    <div class="phone">
      <svg width="38" height="38" viewBox="0 0 24 24" aria-hidden="true"><path fill="#c8283a" d="M6.6 10.8a15.1 15.1 0 0 0 6.6 6.6l2.2-2.2c.3-.3.7-.4 1-.2 1.1.4 2.3.6 3.6.6.6 0 1 .4 1 1V20c0 .6-.4 1-1 1A17 17 0 0 1 3 4c0-.6.4-1 1-1h3.5c.6 0 1 .4 1 1 0 1.3.2 2.5.6 3.6.1.3 0 .7-.2 1z"/></svg>
      017-555-0148
    </div>
    <div class="address">〒030-0000 青森県青森市灯町1-2-3 灯ビル1F</div>
    <div class="pay"><i></i>お支払いは Qペイ 可能です</div>
  </footer>
</div>
</body>
</html>
```